Out of town New Masters of Accounting

size of ad is 7” x 9.6”
please leave one inch on bottom for footer
We want to attract out of town students to join this master's in accounting program.
You DO NOT  have to use a picture of a person.
But if you do, it should be a  male with a white shirt and should not have long hair.(look like a young executive)
THE TEXT OF THE AD IS IN THE ATTACHMENTS
THE CAP LETTERS ARE THE INSTRUCTIONS

The age we are trying to attract is from 20-30 of ages.
- a clear ad .. the text should not take up the entire ad.. it should not be very crowded -
it should be an attractive ad that people would want to see and stand out
- the text very big and take up the entire ad

```html
<!DOCTYPE html>
<html lang="en">
<head>
<meta charset="utf-8">
<title>Remote Masters of Science in Accounting</title>
<link rel="stylesheet" href="https://fonts.googleapis.com/css2?family=Oswald:wght@500&family=Arimo:wght@400;700&family=Montserrat:wght@700;800&display=swap">
<style>
  :root {
    --magenta: #e327e3;
    --violet: #8a35d6;
    --indigo: #4a3cb8;
    --deep-blue: #0a1a9c;
    --panel: rgba(255, 140, 235, 0.28);
    --teal: #2cb5b0;
    --orange: #f29a1c;
    --white: #ffffff;
  }
  * { margin: 0; padding: 0; box-sizing: border-box; }
  html, body { width: 928px; height: 1200px; overflow: hidden; }
  body { font-family: "Arimo", Arial, sans-serif; color: var(--white); }
  .ad {
    position: relative;
    width: 928px;
    height: 1200px;
    overflow: hidden;
    background: linear-gradient(160deg, var(--magenta) 0%, var(--violet) 35%, #5d3cc8 65%, var(--indigo) 100%);
  }
  .headline-panel {
    position: absolute;
    left: 57px; top: 0;
    width: 417px; height: 400px;
    background: var(--panel);
    border-radius: 0 0 34px 34px;
    box-shadow: 0 18px 24px -14px rgba(60, 10, 90, 0.45);
  }
  .headline {
    position: absolute;
    left: 91px; top: 72px;
    width: 370px;
    font-family: "Oswald", "Arial Narrow", sans-serif;
    font-weight: 500;
    font-size: 60px;
    line-height: 73px;
    letter-spacing: -2px;
    white-space: nowrap;
  }
  .headline .kicker { font-size: 62px; margin-left: 4px; letter-spacing: -2.5px; }
  .illustration {
    position: absolute;
    left: 482px; top: 18px;
    width: 421px; height: 492px;
    border-radius: 20px;
    background: radial-gradient(circle at 60% 45%, #6fd0ff 0%, #3b7be8 35%, rgba(120, 70, 230, 0.6) 70%, rgba(160, 60, 220, 0) 100%);
  }
  .pitch { position: absolute; left: 0; width: 928px; text-align: center; }
  .pitch-lead { top: 515px; font-size: 33px; }
  .pitch-degree { top: 556px; font-size: 35px; font-weight: 700; letter-spacing: 0.3px; }
  .pitch-dates { top: 655px; font-size: 32px; }
  .placement-band { position: absolute; left: 0; top: 745px; width: 640px; height: 200px; }
  .placement {
    position: absolute;
    left: 104px; top: 766px;
  }
  .placement h2 {
    font-family: "Arimo", Arial, sans-serif;
    font-weight: 700;
    font-size: 28px;
    line-height: 35px;
    margin-bottom: 6px;
  }
  .placement ul { list-style: none; font-size: 21px; line-height: 25.5px; }
  .placement li::before { content: "\2022"; margin-right: 5px; }
  .duration-seal { position: absolute; left: 633px; top: 720px; width: 254px; height: 254px; }
  .duration-text {
    position: absolute;
    left: 633px; top: 778px;
    width: 254px;
    text-align: center;
    font-family: "Montserrat", Arial, sans-serif;
    font-weight: 700;
  }
  .duration-text .small { font-size: 19px; line-height: 20px; display: block; }
  .duration-text .number { font-size: 86px; font-weight: 800; line-height: 82px; display: block; letter-spacing: -3px; }
  .duration-text .unit { font-size: 21px; line-height: 22px; display: block; }
  .ranking-badge {
    position: absolute;
    left: 138px; top: 990px;
    width: 80px; height: 80px;
    border-radius: 50%;
    background: var(--orange);
  }
  .ranking-note {
    position: absolute;
    left: 260px; top: 1098px;
    font-size: 19px;
    line-height: 23px;
  }
</style>
</head>
<body>
  <main class="ad">
    <div class="headline-panel"></div>
    <h1 class="headline">
      <span class="kicker">ALL NEW!</span><br>
      Remote Program<br>
      for out of town<br>
      Students
    </h1>

    <div class="illustration" role="img" aria-label="Isometric illustration of a young professional at a large laptop surrounded by gears, a target, charts and rising bar graph"></div>

    <p class="pitch pitch-lead">Advance further in your career with a</p>
    <p class="pitch pitch-degree">MASTERS OF SCIENCE IN ACCOUNTING</p>
    <p class="pitch pitch-dates">Beginning August 17 I New lower prices</p>

    <svg class="placement-band" viewBox="0 0 640 200" aria-hidden="true">
      <path d="M0 0 H560 Q585 0 597 25 L640 200 H0 Z" fill="var(--deep-blue)"/>
    </svg>
    <section class="placement">
      <h2>Northgate Career Network Job<br>Placement Advantage</h2>
      <ul>
        <li>96% placement rate</li>
        <li>8 placement coordinators</li>
        <li>Decades of relationships with 100’s of firm</li>
      </ul>
    </section>

    <svg class="duration-seal" viewBox="0 0 254 254" aria-hidden="true">
      <polygon fill="var(--teal)" points="254,127 233.7,143.8 247.8,166.2 223.2,176 229.7,201.7 203.4,203.4 201.7,229.7 176,223.2 166.2,247.8 143.8,233.7 127,254 110.2,233.7 87.8,247.8 78,223.2 52.3,229.7 50.6,203.4 24.3,201.7 30.8,176 6.2,166.2 20.3,143.8 0,127 20.3,110.2 6.2,87.8 30.8,78 24.3,52.3 50.6,50.6 52.3,24.3 78,30.8 87.8,6.2 110.2,20.3 127,0 143.8,20.3 166.2,6.2 176,30.8 201.7,24.3 203.4,50.6 229.7,52.3 223.2,78 247.8,87.8 233.7,110.2"/>
    </svg>
    <p class="duration-text">
      <span class="small">A MASTERS</span>
      <span class="small">IN ONLY</span>
      <span class="number">15</span>
      <span class="unit">MONTHS</span>
    </p>

    <div class="ranking-badge" aria-hidden="true"></div>
    <p class="ranking-note">Halewood University (HU) Master in Accounting Program<br>received the highest possible star rating</p>
  </main>
</body>
</html>
```